KV HOLDWELL GROUP LETTERHEAD

I need letterhead for "KV Holdwell group LLC" ...

logo attached to project...

Company Info:
845 North Marlow Avenue, Suite 7B
Chicago, Illinois 60611
ofc 312-555-0184
facsimile 312-555-0172
www.kvholdwellgroup.example
info@kvholdwellgroup.example

I have multiple projects listed.. see below:

Business cards for ashford lane equity llc
letterhead
envelopes

Business cards for KV Holdwell LLC
letterhead
envelopes

```html
<!DOCTYPE html>
<html lang="en">
<head>
<meta charset="utf-8">
<title>KV Holdwell Group LLC — Letterhead</title>
<link href="https://fonts.googleapis.com/css2?family=Arimo&display=swap" rel="stylesheet">
<style>
  :root {
    --navy: #2f4d79;
    --ink: #231f20;
    --paper: #ffffff;
    --ghost: #e4e5e7;
    --rule-dark: #1d1d1f;
  }
  * { margin: 0; padding: 0; box-sizing: border-box; }
  html, body { width: 928px; height: 1200px; overflow: hidden; background: var(--paper); }
  .letterhead { position: relative; width: 928px; height: 1200px; background: var(--paper); }

  .brand-mark { position: absolute; left: 170px; top: 24px; width: 104px; height: 104px; border-radius: 50%; background: var(--navy); }
  .brand-name {
    position: absolute; left: 40px; top: 168px; width: 410px; text-align: center;
    font-family: "Arimo", sans-serif; font-weight: 400; font-size: 27px; line-height: 32px;
    color: var(--navy); white-space: nowrap;
  }

  .header-band { position: absolute; left: 463px; top: 0; width: 137px; height: 216px; background: var(--navy); }

  .contact {
    position: absolute; right: 29px; top: 52px; text-align: right; font-style: normal;
    font-family: "Arimo", sans-serif; font-size: 17px; line-height: 20.8px; color: var(--ink);
  }

  .rule-primary { position: absolute; left: 0; top: 214px; width: 928px; height: 5px; background: var(--navy); }
  .rule-secondary { position: absolute; left: 0; top: 221px; width: 928px; height: 2px; background: var(--rule-dark); }

  .watermark-mark { position: absolute; left: 334px; top: 470px; width: 260px; height: 260px; border-radius: 50%; background: var(--ghost); }
  .watermark-name {
    position: absolute; left: 0; width: 928px; top: 906px; text-align center; text-align: center;
    font-family: "Arimo", sans-serif; font-weight: 400; font-size: 54px; line-height: 64px;
    color: var(--ghost); white-space: nowrap;
  }
</style>
</head>
<body>
  <main class="letterhead">
    <div class="brand-mark" aria-hidden="true"></div>
    <div class="brand-name">KV Holdwell Group LLC</div>

    <div class="header-band"></div>

    <address class="contact">
      845 North Marlow Avenue, Suite 7B<br>
      Chicago, Illinois 60611<br>
      ofc 312-555-0184<br>
      facsimile 312-555-0172<br>
      www.kvholdwellgroup.example<br>
      info@kvholdwellgroup.example
    </address>

    <div class="rule-primary"></div>
    <div class="rule-secondary"></div>

    <div class="watermark-mark" aria-hidden="true"></div>
    <div class="watermark-name" aria-hidden="true">KV Holdwell Group LLC</div>
  </main>
</body>
</html>
```